Oil and Gas Letterhead Design Tweak

Simple letterhead information and design tweak.

Please note, we don't want to change the design or logo of the letterhead only the small changes mentioned below.

We need to change the company name up top to "Northvale Petrotek FZCO"

Also, we need to include in the footer the following information. I have attached an image of roughly how we would like to have it displayed in the footer.

Footer Details:

Northvale Petrotek FZCO,
Unit No. 2378, FZCO Trade Hub, level No. 1, K&P 7, Dubai, United Arab Emirates
Northvale Petrotek FZCO is registered as a free zone company under the rules & regulations of FZCO

Target Market(s)

O&G Market

Industry/Entity Type

Oil And Gas

Font styles to use
Sans Serif

Colors

Designer to choose colors to be used in the design.

Requirements
Must have
• Change the company name to Northvale Petrotek FZCO
• Include the footer on the bottom of the first and continuation page
Should not have
• Should not change the design or logo of the letterhead, only the specified changes mentioned above

```html
<!DOCTYPE html>
<html lang="en">
<head>
<meta charset="utf-8">
<title>Northvale Petrotek FZCO — Letterhead</title>
<link href="https://fonts.googleapis.com/css2?family=Raleway:wght@500&family=Arimo:wght@400;700&display=swap" rel="stylesheet">
<style>
  :root {
    --backdrop: #d9d9d9;
    --paper: #ffffff;
    --brand-blue: #1a56a6;
    --brand-red: #e41e26;
    --ink: #111111;
  }
  * { margin: 0; padding: 0; box-sizing: border-box; }
  html, body { width: 999px; height: 1200px; overflow: hidden; }
  body { background: var(--backdrop); position: relative; }

  .letterhead {
    position: absolute;
    left: 117px; top: 59px;
    width: 764px; height: 1081px;
    background: var(--paper);
    overflow: hidden;
  }
  .top-bands, .bottom-bands { position: absolute; display: block; }
  .top-bands { left: 0; top: 0; }
  .bottom-bands { left: 555px; bottom: 0; }

  .masthead {
    position: absolute;
    left: 172px; top: 38px;
    display: flex; align-items: center; gap: 14px;
  }
  .masthead__mark {
    width: 22px; height: 22px;
    background: var(--brand-red);
  }
  .masthead__name {
    font-family: "Raleway", sans-serif;
    font-weight: 500;
    font-size: 22.5px;
    letter-spacing: 0.2px;
    color: var(--ink);
    white-space: nowrap;
  }

  .footer {
    position: absolute;
    left: 33px; top: 985px;
    font-family: "Arimo", sans-serif;
    color: var(--ink);
  }
  .footer__company { font-weight: 700; font-size: 14px; margin-bottom: 9px; }
  .footer__address {
    display: flex; font-size: 10.5px; margin-bottom: 6px; white-space: nowrap;
  }
  .footer__address span + span::before {
    content: "|"; display: inline-block; margin: 0 22px;
  }
  .footer__note { font-size: 10.5px; white-space: nowrap; }
</style>
</head>
<body>
  <main class="letterhead">
    <svg class="top-bands" width="764" height="14" viewBox="0 0 764 14" aria-hidden="true">
      <polygon points="0,0 175,0 168,14 0,14" fill="var(--brand-blue)"/>
      <polygon points="238,0 764,0 764,14 245,14" fill="var(--brand-red)"/>
    </svg>

    <header class="masthead">
      <span class="masthead__mark" aria-hidden="true"></span>
      <h1 class="masthead__name">NORTHVALE PETROTEK FZCO</h1>
    </header>

    <footer class="footer">
      <p class="footer__company">Northvale Petrotek FZCO,</p>
      <p class="footer__address">
        <span>Unit No. 2378</span>
        <span>FZCO Trade Hub</span>
        <span>level No. 1, K&amp;P 7</span>
        <span>Dubai</span>
        <span>United Arab Emirates</span>
      </p>
      <p class="footer__note">Northvale Petrotek FZCO is registered as a free zone company under the rules &amp; regulations of FZCO</p>
    </footer>

    <svg class="bottom-bands" width="78" height="14" viewBox="0 0 78 14" aria-hidden="true">
      <polygon points="6,0 38,0 32,14 0,14" fill="var(--brand-blue)"/>
      <polygon points="44,0 72,0 78,14 38,14" fill="var(--brand-red)"/>
    </svg>
  </main>
</body>
</html>
```